Style Template created - Report Accounting and Advisory industry

We need a style template created to set out a report for advice. The report follows <br/><br/>- Cover Page - ( we would need to print to a letter head )<br/>- General Disclaimer<br/>- Space to add Excel Reports in to the document- Maybe inserted Pdf's later<br/>- Action Plan dot points under headings<br/>- List of Strategies to be adopted<br/><br/>Attached is a quick example word doc that needs Custom Style Templates made so that we can quickly format items added. Also the ugly PDF that we currently produce for clients <br/><br/>Red - is our preferred Colour<br/><br/>

Target Market(s)

Accounting / Business / Professionals

Industry/Entity Type

Accounting

Colors
ec1f27

Requirements
Nice to have
• Simple Clean design. Not to busy. Easy to modify the "wording text" in design
Should not have
• Too busy or too much color

```html
<!DOCTYPE html>
<html lang="en">
<head>
<meta charset="utf-8">
<title>Hartwell Lane – Report Style Template</title>
<link href="https://fonts.googleapis.com/css2?family=Open+Sans:ital,wght@0,400;0,600;0,700;1,400&display=swap" rel="stylesheet">
<style>
:root{
  --backdrop:#cfcfcf;
  --paper:#ffffff;
  --brand-red:#b5121b;
  --bright-red:#ec1f27;
  --band-deep:#c4161f;
  --band-soft:#f6c9cc;
  --band-mid:#ef5a62;
  --rose-band:#f4c0c5;
  --ink:#222222;
  --muted:#666666;
  --rule:#d9d9d9;
  --logo-grey:#9a9a9a;
}
*{box-sizing:border-box;margin:0;padding:0}
html,body{width:927px;height:1200px;overflow:hidden}
body{background:var(--backdrop);font-family:"Open Sans",Arial,sans-serif;color:var(--ink);position:relative}

.page{position:absolute;width:243px;height:342px;background:var(--paper);box-shadow:0 4px 12px rgba(0,0,0,.35);overflow:hidden}
.col-1{left:64px}.col-2{left:341px}.col-3{left:612px}
.row-1{top:52px}.row-2{top:431px}.row-3{top:805px}

.running-head{position:absolute;top:8px;right:19px;font-size:3.4px;color:var(--ink)}
.running-head b{font-weight:700}
.page-title{position:absolute;left:20px;right:17px;top:21px;font-size:9px;font-weight:400;color:var(--brand-red);letter-spacing:.1px;padding-bottom:2px;border-bottom:.5px solid var(--rule);text-transform:uppercase}
.page-body{position:absolute;left:21px;right:18px;top:40px;font-size:3.5px;line-height:1.5}
.page-body p{margin-bottom:4px}
.sub-head{font-size:6px;font-weight:400;color:#444;margin:4px 0 1px}
.watermark{position:absolute;left:24px;bottom:28px;width:44px;height:44px;border-radius:50%;background:var(--bright-red);opacity:.06}

.page-footer{position:absolute;left:20px;right:9px;bottom:9px;display:flex;align-items:center;gap:3px}
.footer-brand{font-size:6.5px;color:var(--brand-red);line-height:1;white-space:nowrap}
.footer-brand small{display:block;font-size:1.8px;color:var(--muted);letter-spacing:.2px}
.footer-rule{flex:1;height:.8px;background:var(--brand-red)}
.footer-copy{font-size:2.4px;font-weight:700;white-space:nowrap}
.page-number{width:8px;height:8px;border-radius:50%;background:#9d9d9d;color:#fff;font-size:4px;display:flex;align-items:center;justify-content:center}

.decor{position:absolute;inset:0}

/* cover */
.client-logo{position:absolute;left:27px;top:114px;width:54px;height:46px;background:var(--logo-grey);color:#fff;font-size:5.6px;display:flex;align-items:center;justify-content:center}
.cover-title{position:absolute;left:27px;top:173px;font-size:13.8px;line-height:1.07;font-weight:400;color:var(--bright-red)}
.brand-lockup{position:absolute;text-align:left;color:var(--brand-red)}
.brand-lockup .brand-dot{width:14px;height:14px;border-radius:50%;background:var(--bright-red);margin:0 0 4px 46px}
.brand-lockup .brand-name{font-size:13px;line-height:1}
.brand-lockup .brand-tag{font-size:3.4px;color:var(--muted);letter-spacing:.2px}
.cover-brand{left:111px;top:247px}
.cover-note{position:absolute;right:20px;bottom:12px;font-size:2.4px;color:var(--muted);display:flex;align-items:center;gap:3px}
.cover-note i{width:5px;height:5px;border-radius:50%;border:.5px solid var(--muted)}

/* contents */
.toc-label{font-size:6.5px;color:#333;margin-bottom:6px}
.toc-list{list-style:none}
.toc-list li{display:flex;align-items:baseline;font-size:3.6px;height:8.2px}
.toc-list li.lvl-2{padding-left:4px;font-size:3px}
.toc-list li.lvl-3{padding-left:7px;font-size:3px}
.toc-list li.lvl-1{font-weight:700}
.toc-list .leader{flex:1;border-bottom:.6px dotted #555;margin:0 4px;transform:translateY(-1px)}
.toc-list .num{font-weight:400;font-size:3.4px;width:8px;text-align:right}

/* disclaimer */
.disclaimer{font-size:3.5px;line-height:2.9}
.signature{width:60px;height:20px;margin-top:10px;background:linear-gradient(90deg,#e6e6e6,#f4f4f4)}
.sign-name{font-size:4.2px;font-weight:700;margin-top:2px}
.sign-role{font-size:3.6px;margin-top:4px}

/* tax planning */
.quote-bar{background:#8a8a8a;color:#fff;font-style:italic;font-size:6px;text-align:center;padding:1.5px 0;margin:3px 0 4px}
.red-points{list-style:none;padding-left:12px;color:var(--bright-red);margin-bottom:8px}
.red-points li::before{content:"• "}

.strategy-head{font-size:6.5px;font-weight:600;margin:2px 0 2px -8px;color:#333}
.strategy-head span{display:inline-block;width:8px;font-weight:400}
.strategy-italic{font-style:italic;color:#555;font-size:4px;margin:3px 0 1px}

/* needs */
.lede{font-size:5.2px;color:#777;line-height:1.1;font-weight:600;margin-bottom:6px}
.pie-chart{display:block;margin:0 0 0 -10px}
.legend{display:grid;grid-template-columns:repeat(4,1fr);gap:4px 2px;font-size:2.4px;margin:6px 0 22px}
.legend span{display:flex;align-items:center;gap:2px}
.legend i{width:4px;height:4px;display:inline-block}

/* feature pages */
.photo{background:linear-gradient(135deg,#b9c4cf 0%,#5f6f82 45%,#1f2a3a 100%)}
.feature-photo{height:86px;margin-bottom:6px}
.feature-lede{font-size:5.2px;font-weight:700;color:var(--bright-red);line-height:1.15;margin-bottom:5px}
.table-bands{margin:7px 6px 6px;border-top:.5px solid var(--bright-red)}
.table-bands div{height:10px;margin-top:9px;background:var(--rose-band)}
.split{position:absolute;left:21px;right:18px;top:42px;display:grid;grid-template-columns:85px 1fr;gap:15px}
.split .photo{height:127px}
.split .photo + .photo{margin-top:22px;height:112px}
.split-lede{font-size:6.3px;line-height:1.05;color:#444;margin-bottom:8px}
.split-text{font-size:3.5px;line-height:1.5}
.split-text p{margin-bottom:4px}
.split-text a{color:#1f5aa6;text-decoration:none}
.model-head{font-size:6.5px;color:#333;margin:4px 0 1px}

/* back cover */
.back-brand{left:86px;top:257px}
.back-address{position:absolute;left:28px;right:18px;top:307px;font-size:2.3px;color:var(--muted);line-height:1.7}
.back-address b{color:var(--bright-red);font-weight:400}
</style>
</head>
<body>

<!-- Row 1 -->
<section class="page col-1 row-1 cover">
  <svg class="decor" viewBox="0 0 243 342" aria-hidden="true">
    <g transform="rotate(-38 243 0)">
      <rect x="150" y="30" width="200" height="14" fill="var(--band-soft)"/>
      <rect x="150" y="50" width="200" height="26" fill="var(--band-deep)"/>
      <rect x="150" y="82" width="200" height="5" fill="var(--band-mid)"/>
    </g>
    <g transform="rotate(-38 0 342)">
      <rect x="-90" y="300" width="170" height="18" fill="var(--band-deep)"/>
      <rect x="-90" y="323" width="170" height="4" fill="var(--band-mid)"/>
    </g>
  </svg>
  <div class="client-logo">Client Logo</div>
  <h1 class="cover-title">LOREM IPSUM IS SIMPLY<br>DUMMY HAS BEEN</h1>
  <div class="brand-lockup cover-brand">
    <div class="brand-dot"></div>
    <div class="brand-name">Hartwell Lane</div>
    <div class="brand-tag">CHARTERED ACCOUNTANTS</div>
  </div>
  <div class="cover-note"><i></i>Chartered Accountants</div>
</section>

<section class="page col-2 row-1 contents">
  <h2 class="page-title">Table of Contents</h2>
  <div class="page-body" style="top:49px">
    <div class="toc-label">Contents</div>
    <ul class="toc-list">
      <li class="lvl-1">1. Table of Contents<span class="leader"></span><span class="num">01</span></li>
      <li class="lvl-2">1.1. Executive Summary<span class="leader"></span><span class="num">02</span></li>
      <li class="lvl-3">1.1.1. Our Understanding of Your Needs<span class="leader"></span><span class="num">02</span></li>
      <li class="lvl-1">2. Our Recommendations<span class="leader"></span><span class="num">03</span></li>
      <li class="lvl-2">2.1. Our Approach<span class="leader"></span><span class="num">05</span></li>
      <li class="lvl-3">2.1.1. Budget and Timeframe<span class="leader"></span><span class="num">07</span></li>
      <li>3. Appendix A: About Maple Creek<span class="leader"></span><span class="num">10</span></li>
      <li class="lvl-2">3.1. Appendix B: Selected Client List<span class="leader"></span><span class="num">10</span></li>
      <li class="lvl-3">3.1.1. Appendix C: Our Capabilities<span class="leader"></span><span class="num">11</span></li>
      <li>Appendix D: Our Process<span class="leader"></span><span class="num">12</span></li>
    </ul>
  </div>
  <div class="watermark"></div>
  <footer class="page-footer"><div class="footer-brand">Hartwell Lane<small>CHARTERED ACCOUNTANTS</small></div><div class="footer-rule"></div><div class="footer-copy">© 2020 Hartwell Lane Chartered Accountants</div><div class="page-number">1</div></footer>
</section>

<section class="page col-3 row-1 disclaimer-page">
  <div class="running-head">2020 Tax Planning | <b>Client Name Here</b></div>
  <h2 class="page-title">Superannuation</h2>
  <div class="page-body">
    <p class="disclaimer">Provision of Advice is guided by legislative requirements to be provided in a Statement of Advice. Any and all comments regarding Superannuation are not to be taken as advice rather than statement of factual information about the situation. The statement is not a recommendation to take any action unless that action is required by law. The clients personal situation has not been considered in providing the information. Any action to be taken in relation to the information provided, should take into account the clients personal situation and consideration must be given as to whether action will be appropriate for the clients' objectives and needs. Specific Contribution amounts and SMSF product advice can only be provided under a Statement of Advice by a AFSL Holder.</p>
    <div class="signature" role="img" aria-label="Handwritten partner signature"></div>
    <div class="sign-name">Hartwell Lane</div>
    <div class="sign-role">Chartered Accountants</div>
  </div>
  <div class="watermark"></div>
  <footer class="page-footer"><div class="footer-brand">Hartwell Lane<small>CHARTERED ACCOUNTANTS</small></div><div class="footer-rule"></div><div class="footer-copy">© 2020 Hartwell Lane Chartered Accountants</div><div class="page-number">1</div></footer>
</section>

<!-- Row 2 -->
<section class="page col-1 row-2 purpose">
  <div class="running-head">2020 Tax Planning | <b>Client Name Here</b></div>
  <h2 class="page-title">Purpose of Tax Planning</h2>
  <div class="page-body" style="top:38px">
    <div class="sub-head">Why bother.....???</div>
    <p>Tax planning is the activities taken to minimise tax liabilities to ensure all available allowances, deductions, exclusions and exemptions are working together in the most tax effective manner to reduce the total tax bill.</p>
    <p>The purpose of this report is to provide a recommendation of strategies for you to consider for the year to come. This report is not intended to be our final advice to you, but instead a starting point in educating you on potential opportunities.</p>
    <div class="quote-bar">“If you fail to plan, you are planning to fail”</div>
    <p style="margin-bottom:1px">Tax planning strategies are typically employed to help a business achieve their financial and business goals. The benefits of tax planning are:</p>
    <ul class="red-points">
      <li>Lowering the Amount of taxable income</li>
      <li>Reducing the tax rate</li>
      <li>Allowing greater Control of when taxes get paid</li>
      <li>Better Management of your cashflow</li>
      <li>Eliminating nasty tax surprises</li>
    </ul>
    <div class="sub-head">Recommendations</div>
    <p>We will provide you with a list of Action plans and a further list of ........ The list will be broken down in Short term and Longer Term action. Also list of actions to follow up on .....work on this bit ......</p>
    <div class="sub-head">Basis of Preparation</div>
    <p style="margin-bottom:0">The taxation estimate has been prepared on the basis of information provided by the client. The report is intended for internal tax planning purposes and represents a “What if scenario”. It does not necessarily represent real or intended transactions.</p>
    <p>Hartwell Lane have not performed any tests to verify or validate any of the information provided by the client and accordingly express no assurance as to the outcome indicated.</p>
    <p>To the extent permitted by law we do not accept liability for any loss or damage which any person, other than the client may suffer arising from any negligence on our part. No person should rely on the Taxation estimate without having a full review or audit conducted on the data.</p>
  </div>
  <div class="watermark"></div>
  <footer class="page-footer"><div class="footer-brand">Hartwell Lane<small>CHARTERED ACCOUNTANTS</small></div><div class="footer-rule"></div><div class="footer-copy">© 2020 Hartwell Lane Chartered Accountants</div><div class="page-number">1</div></footer>
</section>

<section class="page col-2 row-2 strategies">
  <div class="running-head">2020 Tax Planning | <b>Client Name Here</b></div>
  <h2 class="page-title">Tax Planning Strategies</h2>
  <div class="page-body" style="left:29px;top:39px">
    <div class="strategy-head"><span>1</span>Solution</div>
    <div class="strategy-italic">AI automated accounting</div>
    <p>LedgerLeaf builds automation in stages on top of its current system to reach full automation thanks to the LedgerLeaf AI. LedgerLeaf AI automates every manual task performed by the user. It starts by connecting to all sources of accounting data such as bank accounts, credit card, webshop or document management systems (CloudBox or Stashr). Based on these datas, LedgerLeaf AI creates bookings and generates financial reports. Finally, LedgerLeaf AI features chat-like interface that allows users to communicate seamlessly with it, viewing it as a trusted advisor over time for all their accounting queries.</p>
    <div class="strategy-italic" style="margin-left:-8px"><span style="display:inline-block;width:8px;font-style:normal">1.1</span>Blockchain software license or Token-as-a-License (TaaL)</div>
    <p>It is possible to create tokens on blockchain that represent software licenses, also known as Token-as-a-Licence (TaaL). LedgerLeaf creates TaaL by using the Corvex official wallet which interacts with the Corvex blockchain. Upon purchase of TaaL, the token holder is free to transfer or sell TaaL using secondary market that is built directly over the blockchain, in our case, the Corvex marketplace. LedgerLeaf checks the validity of a token against the blockchain ensuring that token holders have access to the software. TaaL make distribution and securisation of software licenses easier for software developers. All in all, TaaL has a higher value as a normal software license.</p>
    <div class="strategy-head"><span>2.</span>Pre-ICO Token sale</div>
    <p>To realize this innovative vision, LedgerLeaf is launching a pre-ICO in form of a token sale on Corvex blockchain. 20,000,000 tokens are available to purchase for the price of CHF 0.10 each during a 30-day period to be announced. Tokens represent LedgerLeaf lifelong software licenses and by purchasing enough tokens, holders gain access to LedgerLeaf software. 15,000 tokens give access to LedgerLeaf invoicing or accounting. 20,000 tokens give access to both LedgerLeaf accounting and invoicing. Future customers will still have the opportunity to buy directly yearly or monthly subscriptions to have access to LedgerLeaf.</p>
    <div class="strategy-head" style="margin-left:0">Future plans</div>
    <p>A future ICO is planned between 18 and 24 months after the pre-ICO token sale. This offering will support the development of LedgerLeaf into a fully decentralized, privacy-focused ecosystem of applications. The new model will reward each participant so that a new world with zero administrative tasks becomes reality.</p>
  </div>
  <div class="watermark"></div>
  <footer class="page-footer"><div class="footer-brand">Hartwell Lane<small>CHARTERED ACCOUNTANTS</small></div><div class="footer-rule"></div><div class="footer-copy">© 2020 Hartwell Lane Chartered Accountants</div><div class="page-number">1</div></footer>
</section>

<section class="page col-3 row-2 needs">
  <div class="running-head">2020 Tax Planning | <b>Client Name Here</b></div>
  <h2 class="page-title">Our Understanding of Your Needs</h2>
  <div class="page-body" style="top:41px">
    <p class="lede">LedgerLeaf's mission is to help and support the self-employed and small business owners with</p>
    <svg class="pie-chart" width="215" height="98" viewBox="0 0 215 98" role="img" aria-label="Pie chart of revenue share by country">
      <g font-size="2.8" fill="#555">
        <text x="18" y="22">The Netherlands: 3.0%</text>
        <text x="35" y="28">Belgium: 3.6%</text>
        <text x="42" y="35">UK: 6.0%</text>
        <text x="39" y="42">Austria: 7.8%</text>
        <text x="36" y="49">Australia: 8.5%</text>
        <text x="30" y="66">Germany: 10.1%</text>
        <text x="39" y="81">Ireland: 12.2%</text>
        <text x="158" y="41">Lithuania: 30.5%</text>
        <text x="154" y="73">Czech Republic: 18.3%</text>
      </g>
      <ellipse cx="106" cy="49" rx="38" ry="31" fill="#4a4f9a"/>
      <g transform="translate(106 45) scale(1 .82) rotate(-90)">
        <g fill="none" stroke-width="38">
          <circle r="19" stroke="#6eb6dd" stroke-dasharray="36.4 119.4" stroke-dashoffset="0"/>
          <circle r="19" stroke="#5d91d3" stroke-dasharray="21.8 119.4" stroke-dashoffset="-36.4"/>
          <circle r="19" stroke="#5a6fc7" stroke-dasharray="14.6 119.4" stroke-dashoffset="-58.2"/>
          <circle r="19" stroke="#7064be" stroke-dasharray="12.1 119.4" stroke-dashoffset="-72.8"/>
          <circle r="19" stroke="#8a63c0" stroke-dasharray="10.1 119.4" stroke-dashoffset="-84.9"/>
          <circle r="19" stroke="#a067c0" stroke-dasharray="9.3 119.4" stroke-dashoffset="-95.0"/>
          <circle r="19" stroke="#b76bc0" stroke-dasharray="7.2 119.4" stroke-dashoffset="-104.3"/>
          <circle r="19" stroke="#c86eb6" stroke-dasharray="4.3 119.4" stroke-dashoffset="-111.5"/>
          <circle r="19" stroke="#d9758e" stroke-dasharray="3.6 119.4" stroke-dashoffset="-115.8"/>
        </g>
      </g>
    </svg>
    <div class="legend">
      <span><i style="background:#6eb6dd"></i>Lithuania 30.5%</span>
      <span><i style="background:#5d91d3"></i>Czech Republic 18.3%</span>
      <span><i style="background:#5a6fc7"></i>Ireland 12.2%</span>
      <span><i style="background:#7064be"></i>Germany 10.1%</span>
      <span><i style="background:#8a63c0"></i>Australia 8.5%</span>
      <span><i style="background:#a067c0"></i>Austria 7.8%</span>
      <span><i style="background:#b76bc0"></i>UK 6.0%</span>
      <span><i style="background:#c86eb6"></i>Belgium 3.6%</span>
      <span><i style="background:#d9758e"></i>The Netherlands 3.0%</span>
    </div>
    <div class="sub-head" style="color:#333">Lorem Ipsum</div>
    <p>The bulk of the implementation costs will be defined by discovery. Based on similar CRM implementation projects, we feel expect that the CRM side will be somewhere between 200 and 300 hours, give or take. The wide swing in hours is related to the under-defined nature of both the integration needs and our role in the integration project. Our focus in discovery (as mentioned above) will be to nail down those requirements and our role as it relates to what is needed to integrate the sites with the CRM.</p>
    <p>The bulk of the implementation costs will be defined by discovery. Based on similar CRM implementation projects, we feel expect that the CRM side will be somewhere between 200 and 300 hours, give or take. The wide swing in hours is related to the under-defined nature of both the integration needs and our role in the integration project. Our focus in discovery (as mentioned above) will be to nail down those requirements and our role as it relates to what is needed to integrate the sites with the CRM.</p>
  </div>
  <div class="watermark"></div>
  <footer class="page-footer"><div class="footer-brand">Hartwell Lane<small>CHARTERED ACCOUNTANTS</small></div><div class="footer-rule"></div><div class="footer-copy">© 2020 Hartwell Lane Chartered Accountants</div><div class="page-number">1</div></footer>
</section>

<!-- Row 3 -->
<section class="page col-1 row-3 feature">
  <div class="running-head">THE CLIENT NAME</div>
  <h2 class="page-title">Headline Here</h2>
  <div class="page-body" style="top:42px">
    <div class="photo feature-photo" role="img" aria-label="Photo of a businessman sketching cloud computing arrows on a screen"></div>
    <p class="feature-lede">LedgerLeaf's mission is to help and support the self-employed and small business owners with</p>
    <p>Administrative tasks are cumbersome, time-consuming and often prevent small owners from focusing their time and energy on their business and their customers. They can also be extremely stressful and nerve-wracking for those attempting these tasks for the first time.</p>
    <p>At LedgerLeaf, we envisage accounting for the self-employed and small business owners as being automated and decentralized</p>
    <div class="table-bands" role="img" aria-label="Space for an inserted spreadsheet table"><div></div><div></div><div></div></div>
    <p>LedgerLeaf is based on an innovative license model that uses Token-as-a-License (TaaL). The token represents lifelong software license for LedgerLeaf solutions. The Pre-ICO token sales will enable LedgerLeaf to complete its development of LedgerLeaf AI to deliver fully automatic bookkeeping.</p>
    <p>with leading edge business data access to ensure you have the best available data at your fingertips.</p>
  </div>
  <div class="watermark"></div>
  <footer class="page-footer"><div class="footer-brand">Hartwell Lane<small>CHARTERED ACCOUNTANTS</small></div><div class="footer-rule"></div><div class="footer-copy">© 2020 Hartwell Lane Chartered Accountants</div><div class="page-number">1</div></footer>
</section>

<section class="page col-2 row-3 feature-split">
  <div class="running-head">THE CLIENT NAME</div>
  <h2 class="page-title">Headline Here</h2>
  <div class="split">
    <div>
      <div class="photo" role="img" aria-label="Photo of a businessman drawing a cloud diagram"></div>
      <div class="photo" role="img" aria-label="Close-up photo of a suit and tie beneath a drawn cloud diagram"></div>
    </div>
    <div>
      <p class="split-lede">LedgerLeaf's mission is to help and support the self-employed and small business owners with their administrative tasks so they can focus on what matters -- their business.</p>
      <div class="split-text">
        <p>Administrative tasks are cumbersome, time-consuming and often prevent small owners from focusing their time and energy on their business and their customers. They can also be extremely stressful and nerve-wracking for those attempting these tasks for the first time.</p>
        <p>At LedgerLeaf, we envisage accounting for the self-employed and small business owners as being <a>automated and decentralized</a></p>
        <p>Accounting can and should be done automatically. By connecting to all sources of accounting data such as bank accounts, payment systems, e-commerce websites, and invoicing systems, LedgerLeaf AI automatically completes these tasks, which would take hours to do manually. Bookings are created automatically and fully completed. Financial statements are available within a couple of clicks, and after analysing your data, LedgerLeaf AI will offer you tips to improve your financial stability.</p>
        <p>What may seem like a pipedream to the millions of self-employed who struggle with</p>
        <div class="model-head">The LedgerLeaf model</div>
        <p>LedgerLeaf is based on an innovative license model that uses Token-as-a-License (TaaL). The token represents lifelong software license for LedgerLeaf solutions. The Pre-ICO token sales will enable LedgerLeaf to complete its development of LedgerLeaf AI to deliver fully automatic</p>
      </div>
    </div>
  </div>
  <footer class="page-footer"><div class="footer-brand">Hartwell Lane<small>CHARTERED ACCOUNTANTS</small></div><div class="footer-rule"></div><div class="footer-copy">© 2020 Hartwell Lane Chartered Accountants</div><div class="page-number">1</div></footer>
</section>

<section class="page col-3 row-3 back-cover">
  <svg class="decor" viewBox="0 0 243 342" aria-hidden="true">
    <g transform="rotate(-38 243 0)">
      <rect x="120" y="40" width="240" height="18" fill="var(--band-soft)"/>
      <rect x="120" y="64" width="240" height="34" fill="var(--band-deep)"/>
      <rect x="120" y="104" width="240" height="6" fill="var(--band-mid)"/>
    </g>
  </svg>
  <div class="brand-lockup back-brand">
    <div class="brand-dot" style="margin-left:22px"></div>
    <div class="brand-name" style="font-size:9px">Hartwell Lane</div>
    <div class="brand-tag" style="font-size:2.4px">CHARTERED ACCOUNTANTS</div>
  </div>
  <div class="back-address">
    <b>Brightmere Pty Ltd</b> ACN 100 200 300 • 12 Harbour Lane, Eastfield, WA 6100 • PO Box 2040, Eastfield, WA 6100<br>
    Tel: 08 5550 0140 • Fax: 08 5550 0141 • Email: dana@hartwelllane.example • <b>Director Dana Hartwell</b>
  </div>
</section>

</body>
</html>
```